New Architectural Firm Business Cards

New Business card to compliment previous pixel forum logo (attached). Please design a business card that is simple, modern, creative....please do not use "symbols", simply the logo and associated graphics/text. The front should contain name/address/phone/email/web address (with graphics).....back should be 100% graphic design using the logo somehow. Hoping for a two color (black and yellow) design. full bleed design, no borders

Target Market(s)

Commercial Architecture Clients

Industry/Entity Type

Architecture

Contact Information for Business Card

Please design a business card that is simple, modern, creative....please do not use "symbols", simply the logo and associated graphics/text. The front should contain name/address/phone/email/web address (with graphics).....back should be 100% graphic design using the logo somehow

Font styles to use
Sans Serif

Colors
FFF300
FFF600
FEFA6F
FFFEC7
FFFEE8

Requirements
Must have
• Clean, Modern Design
Should not have
• Stock images or "icons"

```html
<!DOCTYPE html>
<html lang="en">
<head>
<meta charset="utf-8">
<title>Pixel Forum – Business Card Set</title>
<link rel="stylesheet" href="https://fonts.googleapis.com/css2?family=Montserrat:wght@400;500;700;800&display=swap">
<style>
  :root {
    --ink: #2f2d2e;
    --sun: #f5c115;
    --paper: #efeff1;
    --line: #ffffff;
    --backdrop: #f3f3f3;
  }
  html, body {
    margin: 0;
    padding: 0;
    width: 1200px;
    height: 1000px;
    overflow: hidden;
    background: var(--backdrop);
    font-family: "Montserrat", sans-serif;
  }
  .sheet {
    position: relative;
    width: 1200px;
    height: 1000px;
  }
  .card {
    position: absolute;
    width: 451px;
    height: 270px;
    display: block;
  }
  .card--front-dark  { left: 111px; top: 134px; --field: var(--ink); --wedge: var(--sun); --text: #ffffff; }
  .card--back-sun    { left: 651px; top: 134px; --field: var(--ink); --wedge: var(--sun); }
  .card--front-sun   { left: 111px; top: 533px; --field: var(--sun); --wedge: var(--ink); --text: var(--ink); }
  .card--back-dark   { left: 651px; top: 535px; --field: var(--sun); --wedge: var(--ink); }

  .contact { font-size: 13.5px; font-weight: 400; fill: var(--text); }
  .holder-name { font-size: 18px; font-weight: 500; fill: var(--ink); }
  .brand { font-weight: 800; fill: var(--wedge); }
  .brand--small { font-size: 12px; }
  .brand--large { font-size: 30px; }
  .defs { position: absolute; width: 0; height: 0; }
</style>
</head>
<body>
<svg class="defs" aria-hidden="true">
  <defs>
    <symbol id="card-geometry" viewBox="0 0 451 270">
      <rect class="field" width="451" height="270" style="fill: var(--field)"/>
      <polygon class="wedge" points="269,0 451,0 451,270 269,270 404,135" style="fill: var(--wedge)"/>
      <rect class="edge-tab" x="0" y="88" width="32" height="96" style="fill: var(--wedge)"/>
      <line class="hairline" x1="298" y1="0" x2="384" y2="86" stroke="#fff" stroke-width="1.2"/>
      <line class="hairline" x1="340" y1="224" x2="400" y2="164" stroke="#fff" stroke-width="1.2"/>
      <rect class="spark" x="329" y="48" width="8" height="8" fill="#fff" transform="rotate(45 333 52)"/>
      <rect class="spark" x="398" y="157" width="8" height="8" fill="#fff" transform="rotate(45 402 161)"/>
      <line class="stripe" x1="258" y1="252" x2="322" y2="188" stroke-width="5" style="stroke: var(--wedge)"/>
      <line class="stripe" x1="268" y1="262" x2="332" y2="198" stroke-width="5" style="stroke: var(--wedge)"/>
      <rect class="badge" x="288" y="82" width="106" height="106" transform="rotate(45 341 135)" style="fill: var(--paper)"/>
    </symbol>
  </defs>
</svg>

<main class="sheet">
  <!-- Front, dark field -->
  <svg class="card card--front-dark" viewBox="0 0 451 270" aria-label="Business card front">
    <use href="#card-geometry"/>
    <text class="holder-name" x="341" y="141" text-anchor="middle">Mara Quill</text>
    <text class="contact" x="52" y="99">+00 98 76 54 32 10</text>
    <text class="contact" x="52" y="121">hello@mailbox.net</text>
    <text class="contact" x="52" y="140">www.pixelforum.net</text>
    <text class="contact" x="52" y="163">Studio 4, Harbour Lane</text>
    <text class="contact" x="52" y="180">#7 Elm Street, NY-418</text>
  </svg>

  <!-- Back, yellow field -->
  <svg class="card card--back-sun" viewBox="0 0 451 270" aria-label="Business card back">
    <g transform="translate(451 0) scale(-1 1)"><use href="#card-geometry"/></g>
    <text class="brand brand--small" x="110" y="139" text-anchor="middle">Pixel Forum</text>
    <text class="brand brand--large" x="321" y="130" text-anchor="middle">PIXEL</text>
    <text class="brand brand--large" x="321" y="162" text-anchor="middle">FORUM</text>
  </svg>

  <!-- Front, yellow field -->
  <svg class="card card--front-sun" viewBox="0 0 451 270" aria-label="Business card front">
    <use href="#card-geometry"/>
    <text class="holder-name" x="341" y="141" text-anchor="middle">Mara Quill</text>
    <text class="contact" x="52" y="99">+00 98 76 54 32 10</text>
    <text class="contact" x="52" y="121">hello@mailbox.net</text>
    <text class="contact" x="52" y="140">www.pixelforum.net</text>
    <text class="contact" x="52" y="163">Studio 4, Harbour Lane</text>
    <text class="contact" x="52" y="180">#7 Elm Street, NY-418</text>
  </svg>

  <!-- Back, dark field -->
  <svg class="card card--back-dark" viewBox="0 0 451 270" aria-label="Business card back">
    <g transform="translate(451 0) scale(-1 1)"><use href="#card-geometry"/></g>
    <text class="brand brand--small" x="110" y="139" text-anchor="middle">Pixel Forum</text>
    <text class="brand brand--large" x="321" y="130" text-anchor="middle">PIXEL</text>
    <text class="brand brand--large" x="321" y="162" text-anchor="middle">FORUM</text>
  </svg>
</main>
</body>
</html>
```